Pelltab App Analytics Dashboard Design

Our app is designed for visitors centers and hotel/lodging concierges to assist (and allow) travelers to book tours and activities on-site with a kiosk or at front desk. This analytics dashboard will help the hotels or visitors centers owners and employees to understand the activity within their app for their specific business.

We would like this to be modern, clean and sleek and really stand out when we highlight it at an upcoming presentation/conference. The stats we would like to show are:
(By day/month/time period)
Number of Bookings
Source of Bookings i.e. website vs mobile vs kiosk (% of a whole)
Top 5 tour operators booked (and volume of each)
Top 5 tours booked (and volume of each)
Commissions earned (*admin only option - won't show for regular users)

I am including some screen shots of our current Pelltab app to see our general design and color palate. We would like to use this library: https://quillarch.com/open-source/meridian/gallery

This could lead to further UX design improvements for our current app and future projects. I will be paying out a winner and will provide feedback as the contest goes on.

Target Market(s)

Hotel Concierges & Managers, Visitor Bureau Managers and Employees

Industry/Entity Type

Travel Industry

Font styles to use
Other font styles liked:
• Apple Fonts: San Francisco

Requirements
Must have
• We would like to use this library: https://quillarch.com/open-source/meridian/gallery
• The stats we would like to show are:
• (By day/month/time period)
• Number of Bookings
• Source of Bookings i.e. website vs mobile vs kiosk (% of a whole)
• Top 5 tour operators booked (and volume of each)
• Top 5 tours booked (and volume of each)
• Commissions earned (*admin only option - won't show for regular users)
Nice to have
• Would be nice to have an easy way for users to toggle between time periods that are common and also choose dates from drop down calendars.
• Will be used on an Pelltab and Slatebook Max

```html
<!DOCTYPE html>
<html lang="en">
<head>
<meta charset="utf-8">
<title>Pelltab Dashboard</title>
<link rel="stylesheet" href="https://fonts.googleapis.com/css2?family=Roboto:wght@300;400;500;700&display=swap">
<style>
  :root{
    --status:#2a86ad;
    --header:#3092b8;
    --search:#4aa3c6;
    --body:#edf1f4;
    --card:#ffffff;
    --ink:#333a40;
    --muted:#9aa3ab;
    --label:#6f7880;
    --line:#e6eaed;
    --green:#2dbb3c;
    --orange:#f26f4f;
    --track:#eceff1;
    --band:#dbe5eb;
    --accent:#2b88b3;
  }
  *{box-sizing:border-box;margin:0;padding:0}
  html,body{width:1200px;height:952px;overflow:hidden}
  body{font-family:"Roboto",sans-serif;background:var(--body);color:var(--ink);position:relative}
  .status-bar{position:absolute;left:0;top:0;width:1200px;height:24px;background:var(--status);color:#fff;font-size:13px;font-weight:500;display:flex;align-items:center;justify-content:space-between;padding:0 10px}
  .status-bar .left{display:flex;align-items:center;gap:6px}
  .status-bar .right{display:flex;align-items:center;gap:5px}
  .app-header{position:absolute;left:0;top:24px;width:1200px;height:66px;background:var(--header);color:#fff}
  .menu-icon{position:absolute;left:20px;top:22px}
  .search{position:absolute;left:73px;top:18px;width:208px;height:32px;border-radius:16px;background:var(--search);font-size:14px;color:rgba(255,255,255,.75);padding:8px 18px}
  .search svg{position:absolute;right:16px;top:9px}
  .app-title{position:absolute;left:0;right:0;top:18px;text-align:center;font-size:25px;font-weight:400}
  .bell{position:absolute;left:970px;top:20px}
  .badge{position:absolute;left:985px;top:16px;width:16px;height:16px;border-radius:50%;background:var(--orange);font-size:10px;text-align:center;line-height:16px}
  .gear{position:absolute;left:1050px;top:21px}
  .avatar{position:absolute;left:1122px;top:16px;width:36px;height:36px;border-radius:50%;background:linear-gradient(135deg,#c9a98b,#6e7f6a)}
  .caret{position:absolute;left:1168px;top:31px}
  .page-title{position:absolute;left:27px;top:118px;font-size:23px;font-weight:400}
  .page-sub{position:absolute;left:27px;top:152px;font-size:16px;color:var(--muted);font-weight:300}
  .filters{position:absolute;left:617px;top:123px;width:554px;height:53px;background:var(--card);display:flex;align-items:center;font-size:17px;color:var(--label)}
  .filter{height:100%;display:flex;align-items:center;justify-content:space-between;padding:0 14px;border-right:1px solid var(--line)}
  .filter.day{width:185px}
  .filter.month{width:185px}
  .filter.time{flex:1;border-right:none;gap:6px;justify-content:flex-start}
  .filter small{font-size:12px;color:var(--muted)}
  .card{position:absolute;background:var(--card)}
  .bookings{left:28px;top:212px;width:377px;height:277px;text-align:center}
  .bookings .num{margin-top:72px;font-size:60px;font-weight:400;letter-spacing:1px}
  .bookings .lbl{margin-top:50px;font-size:23px;color:var(--muted);font-weight:300}
  .sources{left:420px;top:212px;width:751px;height:277px}
  .card-head{position:absolute;left:21px;top:22px;font-size:16px;font-weight:500;color:var(--label);letter-spacing:.3px}
  .source{position:absolute;top:50px;width:250px;text-align:center}
  .source svg{display:block;margin:0 auto}
  .source .pct{position:absolute;left:0;right:0;top:44px;font-size:36px;font-weight:400}
  .source .pct small{font-size:20px}
  .source .name{margin-top:16px;font-size:23px;color:var(--muted);font-weight:300}
  .divider{position:absolute;top:60px;width:1px;height:148px;background:var(--line)}
  .list{top:507px;height:359px}
  .list.operators{left:28px;width:563px}
  .list.tours{left:607px;width:564px}
  .list ul{list-style:none;position:absolute;left:0;right:0;top:58px}
  .list li{position:relative;height:60px;border-bottom:1px solid var(--line)}
  .list li:last-child{border-bottom:none}
  .mark{position:absolute;left:20px;top:12px;width:34px;height:34px;border-radius:50%}
  .photo{position:absolute;left:12px;top:8px;width:44px;height:44px;border-radius:50%}
  .item-name{position:absolute;left:71px;top:13px;font-size:15px;color:var(--ink)}
  .item-desc{position:absolute;left:71px;top:33px;font-size:12.5px;color:var(--muted)}
  .item-time{position:absolute;right:10px;top:15px;font-size:11.5px;color:var(--muted);text-align:right;line-height:19px}
  .commission{position:absolute;left:0;top:887px;width:1200px;height:65px;background:var(--band);color:var(--accent);font-size:24px;font-weight:700;display:flex;align-items:center;justify-content:space-between;padding:0 28px}
</style>
</head>
<body>
  <div class="status-bar">
    <div class="left">Pelltab
      <svg width="16" height="12" viewBox="0 0 16 12"><path d="M1 4a10 10 0 0 1 14 0M3.5 6.5a6.5 6.5 0 0 1 9 0M6 9a3 3 0 0 1 4 0" fill="none" stroke="#fff" stroke-width="1.6"/></svg>
    </div>
    <div>3:14 PM</div>
    <div class="right">32 %
      <svg width="24" height="12" viewBox="0 0 24 12"><rect x="0.5" y="0.5" width="20" height="11" rx="2" fill="none" stroke="#fff"/><rect x="2" y="2" width="6" height="8" fill="#fff"/><rect x="21.5" y="4" width="2" height="4" fill="#fff"/></svg>
    </div>
  </div>

  <header class="app-header">
    <svg class="menu-icon" width="26" height="20" viewBox="0 0 26 20"><path d="M0 2h26M0 10h26M0 18h26" stroke="#fff" stroke-width="2"/></svg>
    <div class="search">Search...
      <svg width="14" height="14" viewBox="0 0 14 14"><circle cx="6" cy="6" r="4.5" fill="none" stroke="#fff" stroke-width="1.4"/><path d="M9.5 9.5L13 13" stroke="#fff" stroke-width="1.4"/></svg>
    </div>
    <div class="app-title">Dashboard</div>
    <svg class="bell" width="24" height="26" viewBox="0 0 24 26"><path d="M4 19V11a8 8 0 0 1 16 0v8l2 2H2zM9 23a3 3 0 0 0 6 0" fill="none" stroke="#fff" stroke-width="1.6"/></svg>
    <div class="badge">5</div>
    <svg class="gear" width="24" height="24" viewBox="0 0 24 24"><circle cx="12" cy="12" r="3.5" fill="none" stroke="#fff" stroke-width="1.6"/><path d="M12 2l2 3 3.5-1 .5 3.5 3.5 1-1 3.5 1.5 2-3 1.5.5 3.5-3.5.5-1.5 3-3-1.5-3 1.5-1.5-3L4 18.5l.5-3.5-3-1.5L3 11.5 2 8.5l3.5-1L6 4l3.5 1z" fill="none" stroke="#fff" stroke-width="1.4" stroke-linejoin="round"/></svg>
    <div class="avatar" role="img" aria-label="User profile photo"></div>
    <svg class="caret" width="10" height="6" viewBox="0 0 10 6"><path d="M0 0h10L5 6z" fill="#fff"/></svg>
  </header>

  <h1 class="page-title">Dashboard</h1>
  <p class="page-sub">Welcome to admin panel !</p>

  <div class="filters">
    <div class="filter day">day <svg width="10" height="7" viewBox="0 0 10 7"><path d="M0 0h10L5 7z" fill="#444"/></svg></div>
    <div class="filter month">month <svg width="10" height="7" viewBox="0 0 10 7"><path d="M0 0h10L5 7z" fill="#444"/></svg></div>
    <div class="filter time">
      <span>00<small>hh</small></span>
      <svg width="10" height="7" viewBox="0 0 10 7"><path d="M0 0h10L5 7z" fill="#444"/></svg>
      <span>&nbsp;:&nbsp;</span>
      <span>00<small>mm</small></span>
      <svg width="10" height="7" viewBox="0 0 10 7"><path d="M0 0h10L5 7z" fill="#444"/></svg>
    </div>
  </div>

  <section class="card bookings">
    <div class="num">2365</div>
    <div class="lbl">Number of Bookings</div>
  </section>

  <section class="card sources">
    <h2 class="card-head">SOURCE OF BOOKINGS</h2>
    <div class="source" style="left:0">
      <svg width="130" height="130" viewBox="0 0 130 130"><circle cx="65" cy="65" r="56" fill="none" stroke="var(--track)" stroke-width="7"/><circle cx="65" cy="65" r="56" fill="none" stroke="var(--green)" stroke-width="7" stroke-dasharray="228.7 351.9" transform="rotate(-90 65 65)"/></svg>
      <div class="pct">65<small>%</small></div>
      <div class="name">website</div>
    </div>
    <div class="divider" style="left:250px"></div>
    <div class="source" style="left:250px">
      <svg width="130" height="130" viewBox="0 0 130 130"><circle cx="65" cy="65" r="56" fill="none" stroke="var(--track)" stroke-width="7"/><circle cx="65" cy="65" r="56" fill="none" stroke="var(--green)" stroke-width="7" stroke-dasharray="105.6 351.9" transform="rotate(-90 65 65)"/></svg>
      <div class="pct">30<small>%</small></div>
      <div class="name">mobile</div>
    </div>
    <div class="divider" style="left:500px"></div>
    <div class="source" style="left:500px">
      <svg width="130" height="130" viewBox="0 0 130 130"><circle cx="65" cy="65" r="56" fill="none" stroke="var(--track)" stroke-width="7"/><circle cx="65" cy="65" r="56" fill="none" stroke="var(--orange)" stroke-width="7" stroke-dasharray="17.6 351.9" transform="rotate(-90 65 65)"/></svg>
      <div class="pct">5<small>%</small></div>
      <div class="name">kiosk</div>
    </div>
  </section>

  <section class="card list operators">
    <h2 class="card-head">TOP 5 TOUR OPERATORS BOOKED</h2>
    <ul>
      <li><span class="mark" style="background:#d9363e"></span><span class="item-name">Operator’s Name</span><span class="item-desc">Lorem Ipsum is simply dummy text of the...</span><span class="item-time">11:20am<br>07-Jun-2017</span></li>
      <li><span class="mark" style="background:#3b3f44"></span><span class="item-name">Operator’s Name</span><span class="item-desc">Lorem Ipsum is simply dummy text of the...</span><span class="item-time">11:20am<br>07-Jun-2017</span></li>
      <li><span class="mark" style="background:#6bb84a"></span><span class="item-name">Operator’s Name</span><span class="item-desc">Lorem Ipsum is simply dummy text of the...</span><span class="item-time">11:20am<br>07-Jun-2017</span></li>
      <li><span class="mark" style="background:#1f4f8a"></span><span class="item-name">Operator’s Name</span><span class="item-desc">Lorem Ipsum is simply dummy text of the...</span><span class="item-time">11:20am<br>07-Jun-2017</span></li>
      <li><span class="mark" style="background:#222;border-radius:0"></span><span class="item-name">Operator’s Name</span><span class="item-desc">Lorem Ipsum is simply dummy text of the...</span><span class="item-time">11:20am<br>07-Jun-2017</span></li>
    </ul>
  </section>

  <section class="card list tours">
    <h2 class="card-head">TOP 5 TOURS BOOKED</h2>
    <ul>
      <li><span class="photo" role="img" aria-label="Tour photo: evening scene" style="background:linear-gradient(135deg,#3d3a45,#a05a8a)"></span><span class="item-name">Tour’s Name</span><span class="item-desc">Lorem Ipsum is simply dummy text of the...</span><span class="item-time">11:20am<br>07-Jun-2017</span></li>
      <li><span class="photo" role="img" aria-label="Tour photo: hikers under a blue sky" style="background:linear-gradient(180deg,#7fa8cf,#5a6a4a)"></span><span class="item-name">Tour’s Name</span><span class="item-desc">Lorem Ipsum is simply dummy text of the...</span><span class="item-time">11:20am<br>07-Jun-2017</span></li>
      <li><span class="photo" role="img" aria-label="Tour photo: forest trail" style="background:linear-gradient(135deg,#4f7a3a,#2e4a2a)"></span><span class="item-name">Tour’s Name</span><span class="item-desc">Lorem Ipsum is simply dummy text of the...</span><span class="item-time">11:20am<br>07-Jun-2017</span></li>
      <li><span class="photo" role="img" aria-label="Tour photo: elephant safari" style="background:linear-gradient(180deg,#8a8a6a,#c9a23a)"></span><span class="item-name">Tour’s Name</span><span class="item-desc">Lorem Ipsum is simply dummy text of the...</span><span class="item-time">11:20am<br>07-Jun-2017</span></li>
      <li><span class="photo" role="img" aria-label="Tour photo: countryside landscape" style="background:linear-gradient(135deg,#7a7e70,#3f4438)"></span><span class="item-name">Tour’s Name</span><span class="item-desc">Lorem Ipsum is simply dummy text of the...</span><span class="item-time">11:20am<br>07-Jun-2017</span></li>
    </ul>
  </section>

  <footer class="commission">
    <span>Commissions earned :</span>
    <span>$125</span>
  </footer>
</body>
</html>
```